Stationery Design Project

We need letterhead and business cards designed for our consulting firm. Color scheme, mostly deep blue (see logo). We are a commercial consulting work out firm, nationwide (large loans, $10MM and up). Visit our website for more info.
Updates

Project Deadline Extended
Reason: Meeting tomorrow morning to make final final decision. Would like this project to stay open to be able to provide feed back and receive final edits and approve. Thank you!!!

Target Market(s)

High end investors

Industry/Entity Type

Business

Requirements
Must have
• Letterhead must have the logo and the address

4817 Larkmoor Avenue, Suite 210, San Diego, CA 92107
Nice to have
• It would be nice to incorporate a watermark of all or some portion of the logo on the letterhead, or at least for the 2nd sheets.

Maybe our phone number: 858.555.0174
and/or webiste: www.tollandridgecap.example
Should not have
• Target users and audience of this will be men so, frilly or whimsical type designs are not preferred.

```html
<!DOCTYPE html>
<html lang="en">
<head>
<meta charset="utf-8">
<title>Tolland Ridge Capital – Business Card</title>
<link rel="stylesheet" href="https://fonts.googleapis.com/css2?family=Jost:wght@400;500&display=swap">
<style>
  :root {
    --page: #ecebe8;
    --card-white: #ffffff;
    --blue-deep: #0a5aa8;
    --blue-bright: #1f86d6;
    --blue-band: #1a73c4;
    --grey-mark: #6f7276;
    --grey-build-light: #d5d7da;
    --grey-build-dark: #8b8f94;
    --ink: #2c2e31;
    --ink-soft: #55585c;
  }
  * { box-sizing: border-box; margin: 0; padding: 0; }
  html, body { width: 827px; height: 1200px; overflow: hidden; }
  body {
    background: var(--page);
    font-family: "Jost", "Helvetica Neue", Arial, sans-serif;
    position: relative;
  }
  .card {
    position: absolute;
    left: 63px;
    width: 700px;
    height: 400px;
    overflow: hidden;
    box-shadow: 0 6px 18px rgba(0,0,0,0.18);
  }
  /* Back of card */
  .card-back {
    top: 150px;
    background: linear-gradient(180deg, var(--blue-bright) 0%, var(--blue-deep) 100%);
    display: flex;
    align-items: center;
    justify-content: center;
    gap: 14px;
  }
  .card-back .brand-square {
    width: 22px; height: 22px;
    background: #ffffff;
  }
  .card-back .brand-name {
    color: #ffffff;
    font-size: 40px;
    font-weight: 500;
    letter-spacing: 1px;
  }
  /* Front of card */
  .card-front {
    top: 650px;
    background: var(--card-white);
  }
  .brand {
    position: absolute;
    left: 44px;
    top: 50px;
    display: flex;
    align-items: center;
    gap: 10px;
  }
  .brand-square {
    width: 16px; height: 16px;
    background: var(--blue-band);
  }
  .brand-name {
    color: var(--grey-mark);
    font-size: 27px;
    font-weight: 500;
    letter-spacing: 0.5px;
  }
  .person {
    position: absolute;
    right: 48px;
    top: 52px;
    text-align: right;
  }
  .person-name {
    color: var(--blue-deep);
    font-size: 24px;
    font-weight: 500;
  }
  .person-title {
    color: var(--ink-soft);
    font-size: 14px;
    margin-top: 2px;
  }
  .contact {
    position: absolute;
    left: 44px;
    top: 196px;
    color: var(--ink);
    font-size: 13.5px;
    line-height: 1.45;
  }
  .contact .address { font-weight: 500; }
  .contact-row {
    display: flex;
    align-items: center;
    gap: 5px;
    color: var(--ink-soft);
  }
  .contact-row svg { width: 12px; height: 12px; flex: none; }
  .contact-row .spacer { width: 8px; }
  .buildings {
    position: absolute;
    right: 40px;
    bottom: 42px;
    width: 270px;
    height: 130px;
    background: linear-gradient(135deg, var(--grey-build-light) 0%, var(--grey-build-dark) 100%);
  }
  .base-band {
    position: absolute;
    left: 0;
    bottom: 0;
    width: 100%;
    height: 42px;
    background: var(--blue-band);
  }
</style>
</head>
<body>

  <section class="card card-back">
    <span class="brand-square"></span>
    <span class="brand-name">Tolland Ridge Capital</span>
  </section>

  <section class="card card-front">
    <div class="brand">
      <span class="brand-square"></span>
      <span class="brand-name">Tolland Ridge Capital</span>
    </div>

    <div class="person">
      <div class="person-name">Dana Whitlock</div>
      <div class="person-title">President</div>
    </div>

    <div class="contact">
      <div class="address">4817 Larkmoor Avenue, Suite 210,</div>
      <div class="address">San Diego, CA 92107</div>
      <div class="contact-row">
        <svg viewBox="0 0 12 12" aria-hidden="true"><path d="M2.5 1h2l1 2.5-1.3 1a6 6 0 0 0 3.3 3.3l1-1.3L11 7.5v2a1.5 1.5 0 0 1-1.5 1.5A8.5 8.5 0 0 1 1 2.5 1.5 1.5 0 0 1 2.5 1z" fill="#1a73c4"/></svg>
        <span>858.555.0174</span>
        <span class="spacer"></span>
        <svg viewBox="0 0 12 12" aria-hidden="true"><rect x="1" y="4" width="10" height="6" rx="1" fill="#1a73c4"/><rect x="3" y="1" width="6" height="4" fill="#1a73c4"/><rect x="3.5" y="6" width="5" height="1" fill="#fff"/></svg>
        <span>858.555.0189</span>
      </div>
      <div class="contact-row">
        <svg viewBox="0 0 12 12" aria-hidden="true"><rect x="1" y="2.5" width="10" height="7" rx="1" fill="#1a73c4"/><path d="M1.5 3.2 6 6.6l4.5-3.4" stroke="#fff" stroke-width="1" fill="none"/></svg>
        <span>dwhitlock@tollandridgecap.example</span>
      </div>
    </div>

    <div class="buildings" role="img" aria-label="Illustration of three grey office buildings rising above water"></div>

    <div class="base-band"></div>
  </section>

</body>
</html>
```